New Business Card Design Project

I need a clean, professional business card. I'd like it to have some color, but not be wild. We do technology consulting and we have clients large and small who trust us with some of their most important data and projects. Simple but not boring should drive all design proposals. Multicolored and two sided, but with a matte finish, I think.
For more on tone, check out our website: http://quorvantis.example

Target Market(s)

Upper management of respected businesses. Tech savvy, but not "hipster".

Industry/Entity Type

Business

Requirements
Must have
• Files need to be provided in .eps and in .pdf in a manner that allows for easy updates.
Must have Name, Title, Phone, Email, Twitter, Website
Nice to have
• Logo/Name shouldn't be too big. One thing I've read several places is that the bigger the logo, the smaller the brand. A good article on dos and don'ts here: http://www.brindlepost.example/2011/02/business-card-experience.html

```html
<!DOCTYPE html>
<html lang="en">
<head>
<meta charset="utf-8">
<title>Quorvantis Business Card</title>
<link rel="stylesheet" href="https://fonts.googleapis.com/css2?family=Comfortaa:wght@300;400&family=Ubuntu:wght@400;500;700&display=swap">
<style>
  :root {
    --teal: #23849a;
    --teal-dark: #1a6f82;
    --lime: #7bb321;
    --ink: #3a3a3a;
    --muted: #5a5a5a;
    --bar: #d4d4d6;
    --paper: #ffffff;
    --backdrop: #e8e9eb;
  }
  * { box-sizing: border-box; margin: 0; padding: 0; }
  html, body { width: 1200px; height: 851px; overflow: hidden; background: var(--backdrop); }
  .stage {
    position: relative; width: 1200px; height: 851px;
    display: flex; justify-content: center; align-items: center; gap: 80px;
  }
  .card {
    position: relative; width: 340px; height: 540px; overflow: hidden;
    box-shadow: 0 2px 6px rgba(0,0,0,.12);
  }
  .card-front { background: var(--teal); }
  .front-wordmark {
    position: absolute; left: 0; top: 0;
    transform-origin: 0 0;
    transform: translate(34px, 510px) rotate(-90deg);
    font-family: "Comfortaa", sans-serif; font-weight: 300;
    font-size: 52px; letter-spacing: 3px; color: var(--paper);
    white-space: nowrap; line-height: 1;
  }
  .front-pattern {
    position: absolute; right: 0; top: 0; width: 230px; height: 540px;
    background: linear-gradient(160deg, rgba(255,255,255,.10) 0%, rgba(255,255,255,.22) 100%);
  }
  .card-back { background: var(--paper); padding: 34px 30px; }
  .brand {
    display: flex; align-items: center; gap: 10px;
    font-family: "Ubuntu", sans-serif; font-weight: 400;
    font-size: 26px; letter-spacing: 3px; color: var(--muted);
  }
  .brand-square { width: 14px; height: 14px; background: var(--teal); }
  .bar { position: absolute; height: 14px; border-radius: 7px; background: var(--bar); }
  .contact {
    position: absolute; left: 30px; right: 30px; top: 190px;
    text-align: right; font-family: "Ubuntu", sans-serif; color: var(--ink);
  }
  .name { font-size: 30px; font-weight: 700; color: var(--teal-dark); }
  .title { color: var(--lime); font-weight: 500; }
  .detail { font-size: 13px; line-height: 1.45; }
  .social { display: inline-flex; align-items: center; gap: 5px; }
  .social i { width: 11px; height: 11px; background: var(--ink); display: inline-block; }
  .website { margin-top: 14px; font-size: 19px; font-weight: 700; }
  .pattern-area {
    position: absolute; right: 0; bottom: 0; width: 170px; height: 66px;
    background: linear-gradient(135deg, rgba(35,132,154,0) 10%, rgba(35,132,154,.35) 100%);
  }
</style>
</head>
<body>
<main class="stage">
  <section class="card card-front" aria-label="Card front">
    <div class="front-pattern" role="img" aria-label="White dot pattern decoration"></div>
    <div class="front-wordmark">QUORVANTIS</div>
  </section>

  <section class="card card-back" aria-label="Card back">
    <div class="brand"><span class="brand-square"></span>QUORVANTIS</div>

    <span class="bar" style="left:150px;top:100px;width:160px"></span>
    <span class="bar" style="left:190px;top:130px;width:120px"></span>
    <span class="bar" style="left:60px;top:160px;width:250px"></span>

    <div class="contact">
      <div class="name">Dana Whitlock,<span class="title">CEO</span></div>
      <div class="detail">1-800-555-0148, ext.700</div>
      <div class="detail">dana@quorvantis.example</div>
      <div class="detail"><span class="social"><i></i>@DanaWhitlock</span></div>
      <div class="detail"><span class="social"><i></i>Dana Whitlock</span></div>
      <div class="website">www.quorvantis.example</div>
    </div>

    <span class="bar" style="left:30px;top:370px;width:280px"></span>
    <span class="bar" style="left:40px;top:398px;width:150px"></span>
    <span class="bar" style="left:150px;top:424px;width:160px"></span>
    <span class="bar" style="left:60px;top:450px;width:140px"></span>

    <div class="pattern-area" role="img" aria-label="Teal dot pattern decoration"></div>
  </section>
</main>
</body>
</html>
```